WordPress Blog/Website for Athlete Focused Sports Marketing Agency

WordPress Website that Serves two primary purposes:

1) Company Information Website which showcases organization's capabilities and work

2) Highlights, Showcases and Displays key information for athlete clients, aggregates all of the content they are creating(mostly social) and is a key portal for publishing press releases, news updates and more.

Key Criteria for Success:

Easily Updatable
Easy to Navigate
Clean Design that follows the function/form of the organization's brand identity while also incorporating the identity of the athletes.

Supporting Documentation:**These files are also uploaded and attached to this project description**
Creative Brief: https://files.vorteldrive.net/a/lumbrecrest.com/file/d/7Kx2PqRmWtZ4nJvLbHsYcEgAoUi/edit?usp=sharing
Logo Files/Designs are attached. Color Palette can be adjusted as necessary.

WireFrame: (Please use your own judgement and creative liberty's to make something that is a lot better then what I came up with):
https://files.vorteldrive.net/file/d/7Kx2PqRmWtZ4mBcNdFgHjKlQwEr/edit?usp=sharing

Current Website(Incomplete): www.lumbrecrest.com

Thanks!

Industry/Entity Type

It Company

Requirements
Must have
• Social Media Integration: A social feed that aggregates content across all channels for multiple users(all of my athletes)

"News=Blog" Portal that serves as the primary engine for the page's content

Professional Look and Design- it should look like a website, not a blog.

```html
<!DOCTYPE html>
<html lang="en">
<head>
<meta charset="utf-8">
<title>Lumbre &amp; Crest — Athlete Sports Marketing</title>
<link rel="stylesheet" href="https://fonts.googleapis.com/css2?family=Oswald:wght@400;500;700&family=Open+Sans:wght@400;600;700&family=Lora:ital,wght@0,700;1,400&display=swap">
<style>
:root{
  --orange:#f47a20;
  --orange-dark:#d9650f;
  --black:#0d0d0d;
  --charcoal:#1c1c1c;
  --grey:#6b6b6b;
  --light:#f4f4f4;
  --white:#ffffff;
  --text:#555555;
}
*{margin:0;padding:0;box-sizing:border-box}
html,body{width:1200px;height:4103px;overflow:hidden}
body{position:relative;background:var(--white);font-family:"Open Sans",Arial,sans-serif;color:var(--text);font-size:13px;line-height:1.6}
.section{position:absolute;left:0;width:1200px}
.title{position:absolute;left:0;width:100%;text-align:center;font-family:"Oswald",Arial,sans-serif;font-weight:700;font-size:40px;letter-spacing:2px;line-height:1}
.rule{position:absolute;left:450px;width:300px;height:2px}
.rule::after{content:"";position:absolute;left:140px;top:-4px;width:10px;height:10px;transform:rotate(45deg);background:inherit}
.tab{position:absolute;right:40px;width:56px;height:28px;font-family:"Oswald",sans-serif;font-size:11px;text-align:center;line-height:34px;clip-path:polygon(50% 0,100% 100%,0 100%)}
.badge{position:absolute;left:570px;width:60px;height:32px;border-radius:30px 30px 0 0}
.ph{position:absolute}

/* header */
.hero{top:0;height:650px;background:linear-gradient(#1a1a1a,#050505)}
.logo{position:absolute;left:120px;top:18px;display:flex;align-items:center;gap:12px;font-family:"Lora",serif;font-weight:700;font-size:30px;color:var(--orange)}
.logo-mark{width:46px;height:46px;border-radius:50%;background:var(--orange)}
.nav{position:absolute;left:560px;top:28px;display:flex;gap:0}
.nav a{color:#ddd;text-decoration:none;font-size:14px;padding:4px 22px;border-bottom:2px solid transparent}
.nav a.active{color:#fff;border-bottom-color:var(--orange)}
.hero-photo{left:100px;top:95px;width:350px;height:555px;background:linear-gradient(160deg,#3a3a3a,#141414)}
.tile{position:absolute;width:330px;height:265px;background:linear-gradient(150deg,#3b3b3b,#161616);border:2px solid #2a2a2a}
.tile-label{position:absolute;top:10px;padding:6px 10px;background:var(--orange);color:#fff;font-family:"Oswald",sans-serif;font-weight:700;font-size:17px;line-height:1.15;max-width:200px}

/* who we are */
.who{top:650px;height:445px}
.who .title{top:56px;color:var(--orange)}
.who .rule{top:112px;background:var(--orange)}
.who-copy{position:absolute;left:135px;top:150px;width:560px}
.who-copy h2{font-family:"Oswald",sans-serif;font-weight:700;font-size:28px;color:#222;letter-spacing:1px}
.who-copy h3{font-family:"Lora",serif;font-style:italic;font-weight:400;font-size:18px;color:#444;margin-bottom:22px}
.who-copy p{margin-bottom:16px;font-size:13px}
.who-photo{left:720px;top:145px;width:300px;height:300px;background:radial-gradient(circle at 50% 50%,#c9c9c9,#fff 70%)}

/* what we do */
.what{top:1095px;height:685px;background:var(--orange)}
.what .title{top:90px;color:#fff}
.what .rule{top:146px;background:#fff}
.video{left:135px;top:220px;width:555px;height:345px;background:linear-gradient(160deg,#6b7d4a,#2e3a24)}
.video-title{position:absolute;left:0;top:0;width:100%;padding:10px 16px;background:rgba(0,0,0,.55);color:#fff;font-weight:700;font-size:18px}
.video-bar{position:absolute;left:0;bottom:0;width:100%;height:36px;background:rgba(0,0,0,.75)}
.video-bar .play{position:absolute;left:12px;top:9px}
.video-bar .track{position:absolute;left:46px;right:20px;top:16px;height:4px;background:#666}
.video-bar .track span{display:block;width:25%;height:100%;background:var(--orange)}
.what-copy{position:absolute;left:715px;top:220px;width:350px;color:#fff;font-size:13px}
.what-copy p{margin-bottom:18px}
.what-copy a{color:#fff;font-weight:600;text-decoration:none}

/* clients tell */
.tell{top:1780px;height:595px}
.tell .title{top:60px;color:#111}
.tell .rule{top:116px;background:#111}
.card{position:absolute;width:300px;height:150px}
.card .ph{left:0;top:0;width:135px;height:140px;background:linear-gradient(160deg,#b9a48d,#5a4a3c)}
.card-info{position:absolute;left:150px;top:0;font-size:12px;color:#333;line-height:1.9}
.card-info h4{font-family:"Oswald",sans-serif;font-weight:700;color:var(--orange);font-size:15px;letter-spacing:.5px;border-bottom:1px solid #ddd;margin-bottom:4px}
.card-info b{font-weight:600}

/* social */
.social{top:2375px;height:635px;background:var(--black);color:#ccc}
.social .title{top:70px;color:#fff}
.social .rule{top:126px;background:#fff}
.col-head{position:absolute;display:flex;align-items:center;gap:10px;color:#fff;font-family:"Oswald",sans-serif;font-weight:700;font-size:22px}
.col-head i{display:block;width:26px;height:26px;border-radius:50%;background:#fff}
.col-head i.sq{border-radius:3px}
.post{position:absolute;width:470px;height:110px}
.post .ph{left:0;top:0;width:80px;height:80px;background:linear-gradient(160deg,#a58a6b,#4a3a2e)}
.post-body{position:absolute;left:95px;top:0;font-size:12px;line-height:1.55}
.post-meta{color:#999;font-size:11px;margin-bottom:3px}
.post-body a{color:var(--orange);text-decoration:none}
.date{position:absolute;left:0;top:0;width:80px;text-align:center;font-family:"Oswald",sans-serif}
.date .d{display:block;background:var(--orange);color:#fff;font-size:38px;font-weight:700;line-height:58px}
.date .m{display:block;background:#fff;color:#111;font-size:13px;font-weight:700;line-height:24px}
.news-item .post-body{left:95px}
.tweet{position:absolute;left:135px;top:2805px;width:930px;height:85px;background:#2b2b2b;border:1px solid #444}
.tweet-icon{position:absolute;left:18px;top:22px;width:40px;height:40px;border-radius:50%;background:#38a1f3}
.tweet p{position:absolute;left:80px;top:14px;right:20px;font-size:12px;color:#ccc}
.tweet p b{color:var(--orange);font-weight:600}

/* key client */
.key{top:3010px;height:470px}
.key .title{top:70px;color:var(--orange)}
.key .rule{top:126px;background:var(--orange)}
.brands{position:absolute;left:120px;top:170px;width:960px;display:grid;grid-template-columns:repeat(4,240px);grid-auto-rows:110px}
.brand{display:flex;align-items:center;justify-content:center;gap:10px;font-family:"Open Sans",sans-serif;font-weight:700;font-size:24px;color:#2b2b2b}
.brand i{display:block;width:30px;height:30px;border-radius:50%;background:#2b2b2b}

/* contact */
.contact{top:3480px;height:570px;background:var(--orange)}
.contact .title{top:70px;color:#fff}
.contact .rule{top:126px;background:#fff}
.contact-sub{position:absolute;top:136px;width:100%;text-align:center;color:#fff;font-family:"Lora",serif;font-style:italic;font-size:15px}
.map{left:130px;top:175px;width:470px;height:280px;background:linear-gradient(135deg,#e9e4d8,#cfd9c5)}
.enquiry{position:absolute;left:625px;top:175px;width:440px;height:280px;background:var(--charcoal);padding:14px 20px}
.enquiry h4{font-family:"Oswald",sans-serif;font-weight:500;font-size:24px;color:#fff;margin-bottom:12px}
.field{background:#fff;height:32px;font-size:11px;color:#888;padding:7px 10px}
.row{display:flex;gap:12px;margin-bottom:12px}
.row .field{flex:1}
.field.area{height:100px;margin-bottom:12px}
.send{display:inline-block;background:#fff;color:#111;font-family:"Oswald",sans-serif;font-weight:700;font-size:18px;padding:4px 22px}
.info{position:absolute;top:485px;display:flex;gap:10px;color:#fff;font-size:12px;line-height:1.4}
.info svg{flex:none}
.info b{display:block;font-family:"Oswald",sans-serif;font-weight:500;font-size:16px}

/* footer */
.footer{top:4050px;height:53px;background:#fff}
.footer p{position:absolute;left:135px;top:17px;font-size:12px;color:#333}
.socials{position:absolute;right:135px;top:12px;display:flex;gap:6px}
.socials i{display:block;width:28px;height:28px;background:#3b5998}
</style>
</head>
<body>

<header class="section hero">
  <div class="logo"><span class="logo-mark"></span>Lumbre &amp; Crest</div>
  <nav class="nav">
    <a class="active" href="#">Home</a><a href="#">What We Do</a><a href="#">Athletes</a><a href="#">Gallery</a><a href="#">Contact Us</a>
  </nav>
  <div class="ph hero-photo" role="img" aria-label="Photo of a racing cyclist on a road bike"></div>
  <div class="tile" style="left:460px;top:100px" role="img" aria-label="Photo of a cyclist"><span class="tile-label" style="left:0">Athlete Brand Building</span></div>
  <div class="tile" style="left:800px;top:100px" role="img" aria-label="Photo of a sprinter in the starting position"><span class="tile-label" style="right:0">Lifestyle &amp; Sports Marketing</span></div>
  <div class="tile" style="left:460px;top:375px" role="img" aria-label="Photo of a bodybuilder"><span class="tile-label" style="left:0">Marketing &amp; Communications: Planning &amp; Design</span></div>
  <div class="tile" style="left:800px;top:375px" role="img" aria-label="Photo of a boxer training"><span class="tile-label" style="right:0">Product Strategy &amp; Launches</span></div>
</header>

<section class="section who">
  <h1 class="title">WHO WE ARE</h1>
  <div class="rule"></div>
  <div class="who-copy">
    <h2>LUMBRE &amp; CREST MEDIA GROUP</h2>
    <h3>Lumbre Avenue to Crest Avenue - A Full Service Agency</h3>
    <p>We build lasting brands for professional athletes. From first sponsorship to global campaign, our team shapes the story, the image and the voice that fans follow. Every plan starts with the athlete and grows into partnerships that last beyond one season.</p>
    <p>Our studio blends strategy, design and media in one place so that every release, every photo and every post speaks with the same clear voice and reaches the right people.</p>
    <p>We listen first, then we plan, then we deliver work that lifts careers and earns trust on and off the field.</p>
  </div>
  <div class="ph who-photo" role="img" aria-label="Photo of a sprinter crouched at the start line"></div>
  <div class="badge" style="top:413px;background:var(--orange)"></div>
  <div class="tab" style="top:417px;background:var(--orange);color:#fff">TOP</div>
</section>

<section class="section what">
  <h1 class="title">WHAT WE DO</h1>
  <div class="rule"></div>
  <div class="ph video" role="img" aria-label="Video still of a cyclist riding outdoors">
    <div class="video-title">Lorem Ipsum</div>
    <div class="video-bar">
      <svg class="play" width="18" height="18" viewBox="0 0 18 18"><path d="M3 2 L16 9 L3 16 Z" fill="#fff"/></svg>
      <div class="track"><span></span></div>
    </div>
  </div>
  <div class="what-copy">
    <p>We plan complete athlete campaigns that join sponsors, media and fans. Our team writes, designs and launches each step, then tracks the results so every season builds on the last one and the next deal comes easier.</p>
    <p>From press releases to social content, we manage the full flow of news for every athlete we represent and keep each channel fresh, active and on brand every single week.</p>
    <a href="#">Read More &gt;&gt;</a>
  </div>
  <div class="badge" style="top:653px;background:#fff"></div>
  <div class="tab" style="top:657px;background:#fff;color:#111">TOP</div>
</section>

<section class="section tell">
  <h1 class="title">CLIENT'S TELL</h1>
  <div class="rule"></div>
  <div class="card" style="left:125px;top:150px"><div class="ph" role="img" aria-label="Portrait photo of an athlete"></div><div class="card-info"><h4>BIOGRAPHY</h4><b>Name :</b> Rowan Hale<br><b>Game :</b> Cycling<br><b>Age :</b> 29<br><b>Country :</b> Australia</div></div>
  <div class="card" style="left:460px;top:150px"><div class="ph" role="img" aria-label="Portrait photo of an athlete"></div><div class="card-info"><h4>BIOGRAPHY</h4><b>Name :</b> Rowan Hale<br><b>Game :</b> Cycling<br><b>Age :</b> 29<br><b>Country :</b> Australia</div></div>
  <div class="card" style="left:785px;top:150px"><div class="ph" role="img" aria-label="Portrait photo of an athlete"></div><div class="card-info"><h4>BIOGRAPHY</h4><b>Name :</b> Rowan Hale<br><b>Game :</b> Cycling<br><b>Age :</b> 29<br><b>Country :</b> Australia</div></div>
  <div class="card" style="left:125px;top:360px"><div class="ph" role="img" aria-label="Portrait photo of an athlete"></div><div class="card-info"><h4>BIOGRAPHY</h4><b>Name :</b> Mira Solen<br><b>Game :</b> Cycling<br><b>Age :</b> 29<br><b>Country :</b> Australia</div></div>
  <div class="card" style="left:460px;top:360px"><div class="ph" role="img" aria-label="Portrait photo of an athlete"></div><div class="card-info"><h4>BIOGRAPHY</h4><b>Name :</b> Rowan Hale<br><b>Game :</b> Cycling<br><b>Age :</b> 29<br><b>Country :</b> Australia</div></div>
  <div class="card" style="left:785px;top:360px"><div class="ph" role="img" aria-label="Portrait photo of an athlete"></div><div class="card-info"><h4>BIOGRAPHY</h4><b>Name :</b> Rowan Hale<br><b>Game :</b> Cycling<br><b>Age :</b> 29<br><b>Country :</b> Australia</div></div>
  <div class="badge" style="top:563px;background:var(--black)"></div>
  <div class="tab" style="top:567px;background:var(--black);color:#fff">TOP</div>
</section>

<section class="section social">
  <h1 class="title">SOCIAL SHARING</h1>
  <div class="rule"></div>
  <div class="col-head" style="left:135px;top:155px"><i></i>BLOG</div>
  <div class="col-head" style="left:625px;top:155px"><i class="sq"></i>NEWS</div>
  <div class="post" style="left:135px;top:200px"><div class="ph" role="img" aria-label="Blog post thumbnail photo"></div><div class="post-body"><div class="post-meta">10 Mar 2013 &nbsp; | &nbsp; 12 Comments</div>Fresh race notes and training news from our riders this week, with new photos and a short recap of the stage.<br><a href="#">[Read More...]</a></div></div>
  <div class="post" style="left:135px;top:325px"><div class="ph" role="img" aria-label="Blog post thumbnail photo"></div><div class="post-body"><div class="post-meta">10 Mar 2013 &nbsp; | &nbsp; 12 Comments</div>Fresh race notes and training news from our riders this week, with new photos and a short recap of the stage.<br><a href="#">[Read More...]</a></div></div>
  <div class="post news-item" style="left:625px;top:200px"><div class="date"><span class="d">30</span><span class="m">MARCH</span></div><div class="post-body" style="width:340px">New partnership signed for the coming season. Our athletes will join a fresh campaign with launches across every channel.<br><a href="#">[Read More...]</a></div></div>
  <div class="post news-item" style="left:625px;top:325px"><div class="date"><span class="d">30</span><span class="m">MARCH</span></div><div class="post-body" style="width:340px">New partnership signed for the coming season. Our athletes will join a fresh campaign with launches across every channel.<br><a href="#">[Read More...]</a></div></div>
  <div class="badge" style="top:603px;background:#fff"></div>
  <div class="tab" style="top:607px;background:#fff;color:#111">TOP</div>
</section>
<div class="tweet"><span class="tweet-icon"></span><p><b>@Lumbre &amp; Crest Media Group</b> Big weekend ahead for the whole team. Follow along for live updates, race photos and behind the scenes stories from every event we cover this spring, straight from the riders and runners themselves.</p></div>

<section class="section key">
  <h1 class="title">KEY CLIENT</h1>
  <div class="rule"></div>
  <div class="brands">
    <div class="brand"><i></i>Pellow</div>
    <div class="brand">Halden</div>
    <div class="brand">Corvane</div>
    <div class="brand">Ostryn</div>
    <div class="brand">Velmora</div>
    <div class="brand">Quillet</div>
    <div class="brand">Brisko</div>
    <div class="brand"><i></i>Arvo</div>
    <div class="brand"><i></i>Tarnwell</div>
    <div class="brand"><i style="border-radius:3px"></i>Nimbrel</div>
    <div class="brand">Kyomi</div>
  </div>
</section>

<section class="section contact">
  <h1 class="title">CONTACT</h1>
  <div class="rule"></div>
  <p class="contact-sub">Come on, We have introduced ourself much, Just leave a message.</p>
  <div class="ph map" role="img" aria-label="Street map showing the office location"></div>
  <form class="enquiry">
    <h4>ENQUIRY</h4>
    <div class="row"><div class="field">Enter Your Name :</div><div class="field">Enter Your Email :</div></div>
    <div class="field area">Enter Your Message :</div>
    <span class="send">SEND</span>
  </form>
  <div class="info" style="left:130px"><svg width="22" height="30" viewBox="0 0 22 30"><path d="M11 0C5 0 0 5 0 11c0 8 11 19 11 19s11-11 11-19C22 5 17 0 11 0z" fill="#fff"/><circle cx="11" cy="11" r="4" fill="#f47a20"/></svg><div><b>Location :</b>12, Harrow Street, Linmore,<br>444 Country</div></div>
  <div class="info" style="left:410px"><svg width="24" height="24" viewBox="0 0 24 24"><path d="M6 2l4 5-2 3c1 3 3 5 6 6l3-2 5 4-3 4C10 22 2 14 2 5z" fill="#fff"/></svg><div><b>Phone :</b>(000) 555 0143</div></div>
  <div class="info" style="left:660px"><svg width="26" height="20" viewBox="0 0 26 20"><rect width="26" height="20" fill="#fff"/><path d="M0 0 L13 11 L26 0" fill="none" stroke="#f47a20" stroke-width="2"/></svg><div><b>Email :</b>info@lumbrecrest.com</div></div>
  <div class="info" style="left:890px"><svg width="24" height="24" viewBox="0 0 24 24"><circle cx="12" cy="12" r="11" fill="none" stroke="#fff" stroke-width="2"/><path d="M1 12h22M12 1c-5 6-5 16 0 22M12 1c5 6 5 16 0 22" fill="none" stroke="#fff" stroke-width="1.5"/></svg><div><b>Website :</b>www.lumbrecrest.com</div></div>
</section>

<footer class="section footer">
  <p>Copyright © 2013 Lumbre &amp; Crest.com All rights reserved</p>
  <div class="socials"><i></i><i style="background:#1da1f2"></i><i style="background:#0e76a8"></i><i style="background:#dd4b39"></i><i style="background:#3b5998"></i><i style="background:#c4302b"></i></div>
</footer>

</body>
</html>
```